Esthetically Pleasing Core Values and Brand Promise for Accounting Firm

I would like a cohesive design that ties together my core values and brand promise. My firm, Maple Finch Advisory, provides accounting work to small businesses. I prefer modern and clean designs. I want my Core Values and Brand Promise to represent me - sole entrepreneur, married, mother of two kids, modern esthetics, clean lines, organized, colorful (teals, greys, white, yellows)

Industry/Entity Type

Public Accounting

Colors
33b8a4

```html
<!DOCTYPE html>
<html lang="en">
<head>
<meta charset="utf-8">
<title>Maple Finch Advisory – Core Values and Brand Promise</title>
<link href="https://fonts.googleapis.com/css2?family=Montserrat:wght@300;400;500;600;700&display=swap" rel="stylesheet">
<style>
  :root {
    --teal: #33b8a4;
    --teal-deep: #1f7f78;
    --teal-dark: #17535a;
    --teal-pale: #cfe9e5;
    --charcoal: #3a3d40;
    --grey: #55595c;
    --paper: #ffffff;
    --stage: #e8ecee;
    --wood: #b89a78;
  }
  * { box-sizing: border-box; margin: 0; padding: 0; }
  html, body { width: 1200px; height: 899px; overflow: hidden; }
  body { background: var(--stage); font-family: "Montserrat", sans-serif; position: relative; }

  .flyer {
    position: absolute; left: 300px; top: 27px;
    width: 435px; height: 612px;
    transform: scale(1.3793); transform-origin: 0 0;
    background: var(--paper); overflow: hidden;
    box-shadow: 0 4px 14px rgba(0,0,0,.18);
  }
  .photo-desk {
    position: absolute; left: 0; top: 0; width: 435px; height: 340px;
    background: linear-gradient(160deg, #d9d4cc 0%, var(--wood) 45%, #8f7a62 100%);
  }
  .shapes { position: absolute; inset: 0; }
  .photo-screen {
    position: absolute; left: 215px; top: 230px; width: 220px; height: 382px;
  }

  .brand-name {
    position: absolute; left: 12px; top: 196px; width: 200px;
    color: var(--teal); font-weight: 300; letter-spacing: 1px; line-height: 1;
  }
  .brand-name .line-1, .brand-name .line-2 { display: block; font-size: 39px; }
  .brand-name .line-3 { display: block; font-size: 16.5px; margin-top: 4px; letter-spacing: 1.5px; }

  .values-title { position: absolute; left: 12px; top: 322px; color: var(--charcoal); line-height: 1; }
  .values-title .strong { display: block; font-size: 35px; font-weight: 600; }
  .values-title .light { display: block; font-size: 25px; font-weight: 300; margin-top: 4px; letter-spacing: 1px; }

  .value-list { position: absolute; left: 10px; top: 406px; width: 205px; list-style: none; }
  .value { display: flex; gap: 10px; height: 48px; align-items: flex-start; }
  .value-icon { width: 36px; height: 36px; flex: none; border-radius: 50%; display: flex; align-items: center; justify-content: center; }
  .value-icon.teal { background: var(--teal); }
  .value-icon.dark { background: var(--charcoal); }
  .value h3 { font-size: 10.5px; font-weight: 700; color: var(--charcoal); letter-spacing: .3px; margin-top: 1px; }
  .value p { font-size: 7px; line-height: 1.35; color: var(--grey); margin-top: 3px; }

  .promise { position: absolute; left: 228px; top: 336px; width: 198px; color: #fff; }
  .promise-title { font-size: 36px; font-weight: 500; line-height: .98; letter-spacing: .5px; }
  .promise-tag { font-size: 7.6px; margin-top: 7px; font-weight: 500; }
  .service { margin-top: 10px; }
  .service h3 { display: flex; align-items: center; gap: 5px; font-size: 10.5px; font-weight: 700; padding-bottom: 3px; border-bottom: 1px solid rgba(255,255,255,.7); }
  .service p { font-size: 7px; line-height: 1.35; margin-top: 4px; font-weight: 500; }

  .contact { position: absolute; left: 228px; top: 567px; width: 198px; color: #fff; font-size: 6px; font-style: italic; }
  .contact-row { display: flex; align-items: center; gap: 5px; position: absolute; white-space: nowrap; }
  .contact-row.address { left: 0; top: 0; line-height: 1.3; }
  .contact-row.phone { left: 112px; top: 2px; font-size: 7px; font-style: normal; }
  .contact-row.web { left: 0; top: 17px; }
</style>
</head>
<body>
  <article class="flyer">
    <div class="photo-desk" role="img" aria-label="Photo of hands typing on a laptop showing a spreadsheet, on a wooden desk"></div>

    <svg class="shapes" width="435" height="612" viewBox="0 0 435 612" aria-hidden="true">
      <defs>
        <linearGradient id="paleFade" x1="0" y1="0" x2="1" y2="1">
          <stop offset="0" stop-color="#cfe9e5"/>
          <stop offset="1" stop-color="#ffffff"/>
        </linearGradient>
      </defs>
      <polygon points="0,70 305,287 215,352 215,612 0,612" fill="#ffffff"/>
      <polygon points="8,92 8,178 120,178" fill="url(#paleFade)"/>
      <polygon points="240,240 305,287 240,334" fill="url(#paleFade)" opacity=".7"/>
      <polygon points="375,0 435,0 435,55" fill="#33b8a4"/>
    </svg>

    <svg class="photo-screen" width="220" height="382" viewBox="0 0 220 382" role="img" aria-label="Teal-tinted close-up photo of a financial spreadsheet">
      <defs>
        <linearGradient id="screenTint" x1="0" y1="0" x2="1" y2="1">
          <stop offset="0" stop-color="#2a9c90"/>
          <stop offset=".55" stop-color="#1f7f78"/>
          <stop offset="1" stop-color="#17535a"/>
        </linearGradient>
      </defs>
      <polygon points="0,122 220,0 220,382 0,382" fill="url(#screenTint)"/>
    </svg>

    <h1 class="brand-name"><span class="line-1">MAPLE</span><span class="line-2">FINCH</span><span class="line-3">ADVISORY</span></h1>

    <h2 class="values-title"><span class="strong">CORE</span><span class="light">VALUES</span></h2>

    <ul class="value-list">
      <li class="value">
        <span class="value-icon teal"><svg width="18" height="18" viewBox="0 0 18 18"><path d="M9 2 L15 9 H11 V16 H7 V9 H3 Z" fill="none" stroke="#fff" stroke-width="1.4" stroke-linejoin="round"/></svg></span>
        <div><h3>EMPOWER</h3><p>we are dedicated, appreciative and respectful of people's time and purpose.</p></div>
      </li>
      <li class="value">
        <span class="value-icon dark"><svg width="20" height="18" viewBox="0 0 20 18"><g fill="none" stroke="#fff" stroke-width="1.3"><circle cx="10" cy="6" r="3"/><path d="M4 16c0-4 3-6 6-6s6 2 6 6"/><circle cx="4" cy="7" r="2"/><circle cx="16" cy="7" r="2"/></g></svg></span>
        <div><h3>CLIENT FOCUSED</h3><p>we provide a personal service that goes above the standards of professional care.</p></div>
      </li>
      <li class="value">
        <span class="value-icon teal"><svg width="20" height="18" viewBox="0 0 20 18"><g fill="none" stroke="#fff" stroke-width="1.3" stroke-linecap="round"><path d="M10 2V16M6 16H14M3 5H17"/><path d="M1 11L3 5L5 11Z M15 11L17 5L19 11Z"/></g></svg></span>
        <div><h3>RECTITUDE</h3><p>we know the difference between what we have the right to do and what the right thing to do is.</p></div>
      </li>
      <li class="value">
        <span class="value-icon dark"><svg width="18" height="18" viewBox="0 0 18 18"><g fill="none" stroke="#fff" stroke-width="1.3"><circle cx="9" cy="9" r="7.5"/><path d="M10 3L6 10H9L8 15L12 8H9Z" fill="#fff" stroke="none"/></g></svg></span>
        <div><h3>RELENTLESS</h3><p>we believe that the longer we try to do our best, the better we become.</p></div>
      </li>
    </ul>

    <section class="promise">
      <h2 class="promise-title">BRAND<br>PROMISE</h2>
      <p class="promise-tag">Trust, Transparency and Dependability</p>
      <div class="service">
        <h3><svg width="11" height="11" viewBox="0 0 11 11"><rect x=".6" y=".6" width="9.8" height="9.8" fill="none" stroke="#fff" stroke-width="1.1"/><path d="M2.5 5.5L4.8 7.8L10 1.5" fill="none" stroke="#fff" stroke-width="1.6"/></svg>TAX</h3>
        <p>Maple Finch provides all clients with a trusted tax advisor who provides accuracy in all filings and ensures your compliance with all government agencies.</p>
      </div>
      <div class="service">
        <h3><svg width="11" height="11" viewBox="0 0 11 11"><rect x=".6" y=".6" width="9.8" height="9.8" fill="none" stroke="#fff" stroke-width="1.1"/><path d="M2.5 5.5L4.8 7.8L10 1.5" fill="none" stroke="#fff" stroke-width="1.6"/></svg>ACCOUNTING</h3>
        <p>Maple Finch provides all business owners with the financial visibility needed to foster growth and facilitate goals.</p>
      </div>
    </section>

    <address class="contact">
      <div class="contact-row address">
        <svg width="7" height="9" viewBox="0 0 7 9"><path d="M3.5 9C1 5.5 0 4.6 0 3.5a3.5 3.5 0 0 1 7 0C7 4.6 6 5.5 3.5 9Z" fill="#fff"/><circle cx="3.5" cy="3.4" r="1.2" fill="#1f7f78"/></svg>
        <span>1850 W. Harbor Lane,<br>Suite 410 Larkspur, CA 90000</span>
      </div>
      <div class="contact-row phone">
        <svg width="9" height="7" viewBox="0 0 9 7"><path d="M0 2.5C0 .5 9 .5 9 2.5V3H6.5V2H2.5V3H0Z M1.5 3.5H7.5L8.5 7H.5Z" fill="#fff"/></svg>
        <span>555-014-2290</span>
      </div>
      <div class="contact-row web">
        <svg width="7" height="7" viewBox="0 0 7 7"><g fill="none" stroke="#fff" stroke-width=".7"><circle cx="3.5" cy="3.5" r="3.1"/><ellipse cx="3.5" cy="3.5" rx="1.3" ry="3.1"/><path d="M.4 3.5H6.6"/></g></svg>
        <span>www.maplefinchadvisory.com</span>
      </div>
    </address>
  </article>
</body>
</html>
```